Make a medical leaflet for my patients undergoing ankle blocks

I have a very boring text only leaflet I would like to turn into a professional appealing medical leaflet to give to my patients. I would like to get this onto two pages of a4 if possible and its intended for electronic distribution mainly.
This will be for patients so it must be professional.
It must also contain a copyright logo on it and my name near the start (Dr Tobias Wendell) so my colleagues can't use it easily.
Target Market(s)
Patients undergoing surgery
Industry/Entity Type
Medical
Font styles to use
Other font styles liked:
- no idea, you tell me
Requirements
Must have
- the information contained on the attachment
- look professional
- a copyright on it
Nice to have
- the ashbury clinic logo
Should not have
- Any spelling, grammatical or linguistic errors
- Any font less than size 12

```html
<!DOCTYPE html>
<html lang="en">
<head>
<meta charset="utf-8">
<title>Ankle Block – Patient Information</title>
<link href="https://fonts.googleapis.com/css2?family=Lato:ital,wght@0,300;0,400;0,700;0,900;1,400&display=swap" rel="stylesheet">
<style>
  :root {
    --blue: #1a8fc9;
    --white: #ffffff;
  }
  * { margin: 0; padding: 0; box-sizing: border-box; }
  html, body { width: 848px; height: 1200px; overflow: hidden; }
  body { background: var(--blue); font-family: "Lato", sans-serif; color: var(--white); }
  .leaflet { position: relative; width: 848px; height: 1200px; overflow: hidden; background: var(--blue); }
  .hero-photo {
    position: absolute; left: 0; top: 0; width: 848px; height: 410px;
    background:
      radial-gradient(ellipse at 45% 10%, rgba(200,225,245,0.55) 0%, rgba(120,170,215,0.25) 18%, transparent 40%),
      linear-gradient(180deg, #1f3f66 0%, #2a5f8f 45%, #2a7fb5 80%, var(--blue) 100%);
  }
  .brand {
    position: absolute; left: 0; width: 848px; top: 344px;
    display: flex; align-items: center; justify-content: center; gap: 10px;
  }
  .brand-mark { width: 14px; height: 14px; background: var(--white); }
  .brand-name { font-weight: 700; font-size: 22px; line-height: 28px; color: var(--white); }
  .title {
    position: absolute; left: 0; width: 848px; top: 408px;
    text-align: center; font-weight: 700; font-size: 38.5px; line-height: 48px;
  }
  .title sup { font-size: 22px; vertical-align: 13px; }
  .column { position: absolute; top: 468px; }
  .column-left { left: 41px; width: 372px; }
  .column-right { left: 441px; width: 378px; }
  h2 {
    font-weight: 900; font-size: 24.5px; letter-spacing: 4.7px; line-height: 30px;
    text-transform: uppercase;
  }
  h3 {
    font-weight: 900; font-size: 18.5px; letter-spacing: 3.8px; line-height: 24px;
    text-transform: uppercase; margin-top: 9px;
  }
  p { font-size: 20px; line-height: 22.8px; margin-top: 7.6px; }
  .column-left h2 + p { margin-top: 6.6px; }
  .numbered { list-style: none; }
  .numbered li {
    position: relative; padding-left: 23px; font-style: italic;
    font-size: 20px; line-height: 22.8px; margin-top: 12px;
  }
  .numbered li .num { position: absolute; left: 0; }
  .benefits { padding-left: 9px; }
  .benefits li:first-child { margin-top: 7.6px; }
  .options { padding-left: 9px; }
  .options li:first-child { margin-top: 36.6px; }
  .options li:last-child { margin-top: 8px; }
  .risks-heading { margin-top: 14px; }
  .lead { font-weight: 300; margin-top: 11.6px; }
  .risk-list { list-style: none; }
  .risk-list > li.risk {
    position: relative; padding-left: 25px; font-style: italic;
    font-size: 20px; line-height: 22.8px; margin-top: 11.6px;
  }
  .risk-list .num { position: absolute; left: 0; }
  .bullets { list-style: none; }
  .bullets li {
    position: relative; padding-left: 25px; font-weight: 300;
    font-size: 20px; line-height: 22.8px; margin-top: 11px;
  }
  .bullets li::before {
    content: ""; position: absolute; left: 3px; top: 9px;
    width: 6px; height: 6px; border-radius: 50%; background: var(--white);
  }
</style>
</head>
<body>
<main class="leaflet">
  <div class="hero-photo" role="img" aria-label="Surgical team operating in a brightly lit theatre with monitors"></div>

  <div class="brand">
    <span class="brand-mark"></span>
    <span class="brand-name">The Ashbury Clinic</span>
  </div>

  <h1 class="title"><sup>©</sup>Dr Tobias Wendell: Patient Information</h1>

  <section class="column column-left">
    <h2>Ankle Block</h2>
    <p>You are scheduled to have surgery on your foot. It is my normal practice to offer and perform (with your consent) an ankle block. This is an optional injection of numbing liquid to the nerves which supply your foot. The ankle block can be performed when you are awake, sedated or under general anaesthesia.</p>
    <p>The ankle block can be combined with a general anaesthetic and with sedation. It can also be used to allow surgery to be performed with you wide awake in certain cases.</p>
    <p>Having or not having an ankle block does not change the pre operative fasting guidelines you have been given.</p>
    <p>There is a fee for performing an ankle block. Please consult my initial introductory email and terms of business for details</p>

    <h3>What are the benefits?</h3>
    <ol class="numbered benefits">
      <li><span class="num">1.</span>Excellent pain relief - usually 10 - 14 hours (and rarely 24 - 48 hours)</li>
      <li><span class="num">2.</span>Avoiding traditional painkillers which resulting in less post operative nausea and vomiting</li>
    </ol>
  </section>

  <section class="column column-right">
    <ol class="numbered options">
      <li><span class="num">3.</span>The option to avoid a general anaesthetic (if you wish)</li>
      <li><span class="num">4.</span>A faster recovery from the general anaesthetic</li>
      <li><span class="num">5.</span>Certain surgery requires an overnight stay in hospital without an ankle block</li>
    </ol>

    <h2 class="risks-heading">What are the risks?</h2>
    <p class="lead">As with all injections, there is the risk of bruising, bleeding and infection.</p>

    <ol class="risk-list">
      <li class="risk"><span class="num">1.</span>Nerve Damage - Occurs 1 in 5000 nerve blocks.</li>
    </ol>
    <ul class="bullets">
      <li>Creates an area of numbness or weakness/paralysis in some / all the foot.</li>
      <li>Majority of nerve injuries will heal themselves within a year</li>
      <li>There is no treatment to fix it</li>
      <li>If the block has not worn off after 72 hours please let me know.</li>
    </ul>
    <ol class="risk-list">
      <li class="risk"><span class="num">2.</span>Failure - The success rate with ankle blocks is 98 - 99%</li>
    </ol>
    <ul class="bullets">
      <li>Some blocks will fail, partially or totally.</li>
      <li>If total failure, I will discuss repeating the block with your consent.</li>
    </ul>
  </section>
</main>
</body>
</html>
```